Cool business cards

Use my existing logo from sketch harbor (see images I have uploaded) and design a really cool non-stuffy business card. I am a divorce mediator.

```html
<!DOCTYPE html>
<html lang="en">
<head>
<meta charset="utf-8">
<title>Sketch Harbor – Business Cards</title>
<link rel="stylesheet" href="https://fonts.googleapis.com/css2?family=Roboto:wght@400&family=Roboto+Condensed:wght@600&display=swap">
<style>
  :root {
    --backdrop: #c4c4c4;
    --teal: #2f9ea3;
    --green: #3d8865;
    --mid: #369689;
    --paper: #f1f1f1;
    --paper-edge: #7a7a7a;
    --ink-light: #ffffff;
    --ink-soft: #e6f3f0;
    --brand-green: #2d8f6c;
  }
  * { margin: 0; padding: 0; box-sizing: border-box; }
  html, body { width: 1200px; height: 576px; overflow: hidden; }
  body {
    background: var(--backdrop);
    font-family: "Roboto", Arial, sans-serif;
    position: relative;
  }
  .card {
    position: absolute;
    border-radius: 13px;
    overflow: hidden;
    box-shadow: 0 4px 10px rgba(0,0,0,0.25);
  }

  /* Front */
  .card-front {
    left: 82px; top: 139px; width: 485px; height: 293px;
    background: linear-gradient(120deg, var(--teal) 0%, var(--mid) 45%, var(--green) 100%);
  }
  .card-front .brand-name {
    position: absolute; left: 0; right: 0; top: 122px;
    text-align: center;
    color: var(--ink-light);
    font-size: 36px; font-weight: 400; letter-spacing: 1px;
    line-height: 44px;
  }

  /* Back */
  .card-back {
    left: 602px; top: 138px; width: 480px; height: 291px;
    background: linear-gradient(120deg, var(--mid) 0%, var(--teal) 40%, var(--green) 100%);
  }
  .card-back .panel { position: absolute; inset: 0; }
  .person-name {
    position: absolute; left: 22px; top: 38px;
    font-family: "Roboto Condensed", "Arial Narrow", sans-serif;
    font-weight: 600; font-size: 20px; line-height: 24px;
    color: var(--ink-light);
  }
  .person-role {
    position: absolute; left: 22px; top: 66px;
    font-size: 12px; color: var(--ink-soft);
  }
  .contact-list {
    position: absolute; left: 22px; top: 194px;
    list-style: none;
    color: var(--ink-soft); font-size: 12.5px;
  }
  .contact-list li { display: flex; align-items: center; height: 18.5px; }
  .contact-list svg { width: 11px; height: 11px; margin-right: 13px; }
  .address {
    position: absolute; left: 25px; top: 254px;
    font-size: 12.5px; color: var(--ink-soft);
  }
  .card-back .brand-name {
    position: absolute; left: 380px; top: 146px;
    transform: translate(-50%, -50%) rotate(-90deg);
    white-space: nowrap;
    color: var(--brand-green);
    font-size: 30px; font-weight: 400; letter-spacing: 1px;
  }
</style>
</head>
<body>

<section class="card card-front">
  <div class="brand-name">Sketch Harbor</div>
</section>

<section class="card card-back">
  <svg class="panel" viewBox="0 0 480 291" preserveAspectRatio="none">
    <path d="M306 0 Q232 145 302 291 L480 291 L480 0 Z" fill="var(--paper-edge)"/>
    <path d="M312 0 Q240 145 310 291 L480 291 L480 0 Z" fill="var(--paper)"/>
  </svg>

  <div class="person-name">Jamie Rowan Hale</div>
  <div class="person-role">Managing Director</div>

  <ul class="contact-list">
    <li>
      <svg viewBox="0 0 12 12"><path d="M1 4 Q6 0 11 4 L9 5 L8 3.5 Q6 3 4 3.5 L3 5 Z M3 6 H9 L10 10 H2 Z" fill="#e6f3f0"/></svg>
      555-014-2270
    </li>
    <li>
      <svg viewBox="0 0 12 12"><rect x="0.5" y="2.5" width="11" height="7" fill="#e6f3f0"/><path d="M0.5 2.5 L6 6.5 L11.5 2.5" stroke="#369689" fill="none"/></svg>
      jamie@sketchharbor.net
    </li>
    <li>
      <svg viewBox="0 0 12 12"><circle cx="6" cy="6" r="5" fill="none" stroke="#e6f3f0" stroke-width="1.2"/><path d="M1 6 H11 M6 1 Q3 6 6 11 Q9 6 6 1" stroke="#e6f3f0" fill="none"/></svg>
      www.sketchharbor.net
    </li>
  </ul>
  <div class="address">48 Quiet Lane, Fairview, US 104826</div>

  <div class="brand-name">Sketch Harbor</div>
</section>

</body>
</html>
```